New telco company needs a product page

We need to design two pages - one index and one inner.

We are a new telco company and we have developed our own phone. We will be selling our services and the phone on this site.

The design should be easy to understand and use, following the latest trends in Web design, be clean. It should communicate professionalism and integrity.

The name of our company is VORO which stands for Value Over Rush Often. The design should follow this principle.

Our company logo is attached. I can send it in other colors/sizes - let me know.

Target Market(s)

Aging population (70+), middle-aged with parents and grandparents.

Industry/Entity Type

It Company

Requirements
Must have
• index page, inner page, flat, clean, Pellucor 5 style / ZEB style (quintel.example), easy navigation, fluid layout, CSS, tableless
Should not have
• should not use old fonts, should not use old-style design, should not have animation, should not look like QDX or Bimzo (too busy)

```html
<!DOCTYPE html>
<html lang="en">
<head>
<meta charset="utf-8">
<title>Voro — Launching Soon</title>
<link href="https://fonts.googleapis.com/css2?family=Lato:wght@300;400;700&display=swap" rel="stylesheet">
<style>
:root{
  --ink:#111;
  --text:#333;
  --muted:#999;
  --rule:#dedede;
  --dot:#aaa;
  --badge:#9a9a9a;
  --tab:#d9d9d9;
  --accent:#e05a55;
  --bg-top:#fbfbfb;
  --bg-bottom:#efefef;
  --screen:#26292c;
  --white:#fff;
}
*{margin:0;padding:0;box-sizing:border-box}
html,body{width:1200px;height:912px;overflow:hidden}
body{font-family:'Lato',sans-serif;color:var(--text);background:var(--white);position:relative}
.site-header{position:absolute;left:0;top:0;width:1200px;height:78px;background:var(--white);border-bottom:1px solid var(--rule)}
.header-pointer{position:absolute;left:571px;top:0}
.header-notch{position:absolute;left:574px;top:77px}
.brand{position:absolute;left:199px;top:18px;display:flex;align-items:center;gap:8px}
.brand-name{font-weight:300;font-size:40px;letter-spacing:-1px;color:var(--ink);line-height:1}
.brand-dot{width:12px;height:12px;border-radius:50%;background:var(--dot);margin-top:14px}
.main-nav{position:absolute;top:31px;left:555px}
.main-nav a{position:absolute;white-space:nowrap;font-size:12px;color:var(--muted);text-decoration:none;padding-left:9px}
.main-nav a::before{content:"";position:absolute;left:0;top:6px;width:4px;height:4px;border-radius:50%;background:var(--muted)}
.main-nav a.active{color:var(--ink)}
.main-nav a.active::before{background:var(--ink)}
.stage{position:absolute;left:0;top:79px;width:1200px;height:778px;background:linear-gradient(var(--bg-top),var(--bg-bottom))}
.badge-rule{position:absolute;top:73px;height:0;border-top:1px dotted #ccc;width:130px}
.badge{position:absolute;left:557px;top:33px;width:82px;height:82px;border-radius:50%;background:var(--badge);color:var(--white);font-size:11px;font-weight:700;text-align:center;display:flex;align-items:center;justify-content:center;line-height:1.25;letter-spacing:-0.3px}
.headline{position:absolute;left:0;width:1200px;top:127px;text-align:center;font-weight:300;color:var(--text)}
.headline .lead{display:block;font-size:18px;letter-spacing:-0.3px}
.headline .with{font-size:18px}
.headline .big{font-size:36px;color:var(--ink);letter-spacing:-1.2px}
.headline .second{display:block;margin-top:-8px}
.device{position:absolute;left:490px;top:205px;width:218px;height:464px;border-radius:30px;background:linear-gradient(180deg,#fdfdfd,#e6e6e6);border:2px solid #d5d5d5;box-shadow:0 6px 6px -4px rgba(0,0,0,.4)}
.device-screen{position:absolute;left:14px;top:63px;width:188px;height:332px;background:var(--screen);border-radius:2px}
.order-cta{position:absolute;left:0;width:1200px;top:706px;text-align:center;font-weight:300;font-size:36px;letter-spacing:-1.5px;color:var(--ink);display:flex;justify-content:center;align-items:center;gap:10px}
.order-cta svg{flex:none}
.features-tab{position:absolute;left:199px;top:748px;width:134px;height:30px;background:var(--tab);border-radius:3px 3px 0 0;font-size:15px;letter-spacing:-0.6px;color:var(--text);display:flex;align-items:center;justify-content:center;gap:10px}
.pager{position:absolute;left:925px;top:755px;display:flex;gap:6px}
.pager span{width:11px;height:11px;border-radius:50%;background:#d4d4d4}
.pager span.current{background:var(--ink)}
.site-footer{position:absolute;left:201px;top:879px;font-size:10px;color:var(--text)}
.site-footer a{color:var(--muted);text-decoration:none}
.site-footer .sep{color:#bbb;margin:0 5px}
</style>
</head>
<body>
<header class="site-header">
  <svg class="header-pointer" width="18" height="9" viewBox="0 0 18 9"><path d="M0 0h18L9 9z" fill="#111"/></svg>
  <div class="brand"><span class="brand-name">voro</span><span class="brand-dot"></span></div>
  <nav class="main-nav">
    <a class="active" href="#" style="left:0">Home</a>
    <a href="#" style="left:59px">Products</a>
    <a href="#" style="left:134px">Features</a>
    <a href="#" style="left:211px">Pricing</a>
    <a href="#" style="left:277px">About Us</a>
    <a href="#" style="left:359px">Contact Us</a>
  </nav>
</header>
<main class="stage">
  <div class="badge-rule" style="left:389px"></div>
  <div class="badge-rule" style="left:678px"></div>
  <div class="badge">LAUNCHING<br>SOON</div>
  <h1 class="headline">
    <span class="lead">The biggest thing to happen in Telecomunication Industry</span>
    <span class="second"><span class="with">with </span><span class="big">New Amazing Features</span></span>
  </h1>
  <div class="device">
    <div class="device-screen" role="img" aria-label="Phone home screen with wallpaper photo, clock and app icons"></div>
  </div>
  <div class="order-cta">
    <svg width="36" height="34" viewBox="0 0 36 34"><path d="M10 12L17 3M26 12L19 3" stroke="var(--accent)" stroke-width="3" fill="none" stroke-linecap="round"/><path d="M2 12h32l-4 20H6z" fill="none" stroke="var(--accent)" stroke-width="3" stroke-linejoin="round"/><path d="M6 19h24M8 25h20" stroke="var(--accent)" stroke-width="3"/></svg>
    <span>Start Ordering Process</span>
    <svg width="22" height="24" viewBox="0 0 22 24"><path d="M2 2l10 10L2 22M9 2l10 10L9 22" stroke="#999" stroke-width="1" fill="none"/></svg>
  </div>
  <div class="features-tab">FEATURES <svg width="14" height="9" viewBox="0 0 14 9"><path d="M2 7l5-5 5 5" stroke="#222" stroke-width="2.5" fill="none"/></svg></div>
  <div class="pager"><span class="current"></span><span></span><span></span><span></span></div>
</main>
<svg class="header-notch" width="50" height="20" viewBox="0 0 50 20"><path d="M0 1h14q9 0 11 17q2-17 11-17h14" fill="#fafafa" stroke="#dedede"/></svg>
<footer class="site-footer">Copyright © 2013Voro.&nbsp; All rights reserved.&nbsp;&nbsp; <a href="#">Terms of Use</a><span class="sep">|</span><a href="#">Privacy Policy</a></footer>
</body>
</html>
```